High Tech - Energy Efficiency Startup needs new look / feel for website

We are a high tech company focused on offering software, services and training courses aimed to create, design and optimize efficient Turbomachinery ( Think: Power Generation, Aerospace, Automotive, Oil & Gas, etc)

I am looking for somebody to design a new front page and 1 second level page. Then we will need to receive the photoshop files.

Here is what our website currently looks like:

www.brevolank.com

here is our work in progress which is not quite there: ua.brevolank.com << Look here for 1st and 2nd level, you will see they look different.

here is what we want it to look like in terms of look and feel and slickness...( our competitors)

www.Kortel.com
http://pqlworkshop.com

You can email questions to Desmond.Ruttle@brevolank.com
Updates

Hello All,

Several things I wanted to note / add:

1) For the Top Menu, we want to add another Item. "Industries" ( same way as Kortel has it)
2) If you find other features which you think we missed or would make sense...

Cheers,

Desmond

Reason: we have two top designs, but they are still not 100% perfect. I hope that somebody will step up and make something which will be truly amazing!

Reason: we still do not confident ending a project that's not 100% complete.

Industry/Entity Type

Training

Requirements
Must have
• If you look at our attempt to have a banner and then smaller sub squares.

The idea is that the banner moves, left to right and displayes larger version of the commercial in the little squares underneath

We need graphics for the banners. They should relate / correspond to the product / or services that is being displayed.

You can see our products and services on ua.brevolank.com so the banners should correlate.

We are really going for minimal words, good graphics, slick and sexy web 2.0 100,00o person company look and feel.

The design / designer who wins, will be given an offer to work with us afterwords and design the rest of our online properties, as well as all of our marketing material.

Please with your application submit your hourly rate for contract work.

```html
<!DOCTYPE html>
<html lang="en">
<head>
<meta charset="utf-8">
<title>Brevolank – Conceptual Design and Optimization of Turbomachinery</title>
<link href="https://fonts.googleapis.com/css2?family=Open+Sans:ital,wght@0,400;0,600;0,700;1,400&family=PT+Sans+Narrow:wght@400;700&display=swap" rel="stylesheet">
<style>
:root{
  --blue:#1d5a9c;
  --blue-dark:#0f3f78;
  --link:#1f4f8c;
  --text:#555;
  --muted:#888;
  --orange:#f08a1c;
  --red:#e2572b;
  --nav:#1e1e1e;
  --footer:#2c2c2c;
  --footer-bottom:#1f1f1f;
  --line:#e2e2e2;
  --page:#fff;
}
*{box-sizing:border-box;margin:0;padding:0}
html,body{width:672px;height:1200px;overflow:hidden}
body{position:relative;background:var(--page);font-family:"Open Sans",Arial,sans-serif;color:var(--text);font-size:7px;line-height:1.55}
a{color:var(--link);text-decoration:none}
ul{list-style:none}
.abs{position:absolute}

/* header */
.brand{left:89px;top:11px;font-weight:700;font-size:15px;line-height:20px;color:var(--blue-dark)}
.tagline{left:89px;top:44px;font-style:italic;font-size:8px;color:#222}
.utility{left:406px;top:4px;height:10px;display:flex;align-items:center;gap:3px}
.social-dot{width:8px;height:8px;background:#3a6fb0;border-radius:1px}
.utility-bar{left:458px;top:0;width:124px;height:17px;background:#eee;border:1px solid #ddd;border-top:0;display:flex;align-items:center;font-size:6.5px;color:#888}
.utility-bar span{padding:0 6px;border-right:1px solid #d6d6d6}
.utility-bar span:last-child{border:0}
.contact{left:500px;top:29px;font-size:7px;color:var(--blue-dark);line-height:1.4}
.contact .phone{font-size:10px;font-weight:700}
.contact svg{vertical-align:middle;margin-right:4px}

/* nav */
.main-nav{left:79px;top:64px;width:514px;height:26px;background:linear-gradient(#3a3a3a,var(--nav));border-radius:3px 3px 0 0;display:flex}
.main-nav a{color:#fff;font-size:8px;display:flex;align-items:center;padding:0 16px;border-right:1px solid #444}
.main-nav a:nth-child(1){width:80px}.main-nav a:nth-child(2){width:111px}.main-nav a:nth-child(3){width:80px}.main-nav a:nth-child(4){width:76px}
.main-nav a:last-child{border-right:0}

/* hero */
.hero-frame{left:79px;top:90px;width:514px;height:268px;border:1px solid #ddd;border-top:0;border-radius:0 0 4px 4px;background:#fff}
.hero{left:86px;top:96px;width:500px;height:196px;background:linear-gradient(100deg,#5a5a5a,#3c3c3c 50%,#2a2a2a)}
.hero-title{left:106px;top:130px;font-family:"PT Sans Narrow",Arial,sans-serif;font-weight:400;color:#fff;font-size:19.5px;line-height:1.2}
.hero-list{left:108px;top:190px;color:#fff;font-size:8px;line-height:1.45}
.btn{display:flex;align-items:center;justify-content:center;color:#fff;font-size:8px;border-radius:2px}
.btn-blue{background:linear-gradient(#2f78c8,#16509a)}
.btn-orange{background:linear-gradient(#ffa23a,#e97a10)}
.hero-shot{left:350px;top:122px;width:211px;height:143px;background:linear-gradient(135deg,#f4f4f4,#d8dce4 55%,#c26a6a);border:1px solid #999}
.thumbs{left:86px;top:300px;width:500px;height:46px}
.thumb{position:absolute;top:1px;width:81px;height:44px;background:linear-gradient(#3b3b3b,#1d1d1d);border:2px solid #444;border-radius:2px}
.thumb.active{border-color:#222}
.thumb.active::after{content:"";position:absolute;left:34px;top:-7px;border:5px solid transparent;border-bottom-color:#222}

/* welcome */
h2{font-weight:400;color:var(--blue-dark);font-size:11px}
.welcome{left:89px;top:374px;width:360px}
.welcome p{margin-top:6px;font-size:6.5px;line-height:1.75}
.more{color:var(--link);font-weight:600}
.demo{left:466px;top:375px;width:117px;height:141px;border:1px solid #ddd;border-radius:3px;box-shadow:0 1px 3px rgba(0,0,0,.12)}
.demo-head{height:22px;display:flex;align-items:center;gap:4px;padding-left:8px;border-bottom:1px solid #e3e3e3;font-size:7.5px;color:var(--blue-dark);font-weight:600;background:linear-gradient(#fff,#f1f1f1)}
.demo p{padding:6px 8px 0;font-size:6px;line-height:1.45;color:#666}

/* columns */
.column h2{margin-bottom:9px}
.edu{left:90px;top:546px;width:155px}
.edu li{font-size:6.5px;color:var(--link);margin-bottom:6px;line-height:1.35}
.edu li::before{content:"• "}
.small-link{font-size:6px;color:var(--link)}
.quote-box{left:257px;top:570px;width:155px;height:96px;border:1px solid #ddd;border-radius:3px;padding:8px 10px;text-align:center;font-size:6.6px;line-height:1.55;color:#666}
.quote-mark{position:absolute;left:5px;top:-4px;font-size:26px;color:#ddd;font-family:Georgia,serif}
.client-name{left:257px;top:685px;font-weight:700;font-size:9px;color:#2a9aa8}
.client-role{left:257px;top:699px;font-size:6px;font-style:italic}
.client-role b{color:var(--link);font-weight:600}
.dots{left:388px;top:555px;display:flex;gap:2px}
.dots i{width:4px;height:4px;border-radius:50%;background:#ccc}
.dots i:first-child{background:var(--blue)}
.feed{left:425px;top:546px;width:160px}
.tweet{display:flex;gap:7px;margin-bottom:9px;font-size:6.6px;line-height:1.55}
.tweet svg{flex:none;margin-top:3px}

/* cards */
.card{top:769px;height:221px;border:1px solid #e4e4e4;box-shadow:0 1px 4px rgba(0,0,0,.12);background:#fff;padding:9px 12px}
.news{left:89px;width:241px}
.papers{left:341px;width:242px}
.card h2{margin-bottom:10px;font-size:11px}
.news-item{display:flex;gap:8px;margin-bottom:10px}
.date{flex:none;width:19px;height:23px;background:var(--red);color:#fff;text-align:center;line-height:1;padding-top:2px}
.date b{display:block;font-size:8.5px}
.date span{font-size:5.5px}
.news-item h3{font-size:6.8px;font-weight:600;color:#333;line-height:1.35}
.news-item p{font-size:5.7px;line-height:1.4;margin-top:1px}
.paper{display:flex;gap:8px;margin-bottom:8px;font-size:5.8px;line-height:1.45}
.paper-icon{flex:none;width:11px;height:12px;border:1px solid #aaa;margin-top:2px;background:#f3f3f3}
.download{display:flex;align-items:center;gap:4px;color:var(--link);margin-top:2px}
.download i{width:6px;height:7px;background:#d33}

/* footer */
.footer{left:0;top:1030px;width:672px;height:142px;background:var(--footer)}
.footer-col{top:1044px;width:120px}
.footer-col h4{font-weight:400;font-size:6.5px;color:#ddd;margin-bottom:6px}
.footer-col li{font-size:6px;color:#999;line-height:2.05}
.footer-col li::before{content:"› ";color:#777}
.footer-bottom{left:0;top:1172px;width:672px;height:28px;background:var(--footer-bottom);font-size:6px;color:#777}
.footer-bottom .copy{position:absolute;left:89px;top:11px}
.footer-bottom .social{position:absolute;left:470px;top:8px;display:flex;align-items:center;gap:6px}
.footer-bottom .social i{width:11px;height:11px;background:#555;border-radius:1px}
</style>
</head>
<body>

<header>
  <div class="abs brand">Brevolank</div>
  <div class="abs tagline">Conceptual Design and Optimization of Turbomachinery</div>
  <div class="abs utility"><i class="social-dot"></i><i class="social-dot"></i><i class="social-dot" style="background:#e67a1e"></i><i class="social-dot"></i></div>
  <div class="abs utility-bar"><span>⌕ Search</span><span>English ▾</span><span>Login</span></div>
  <div class="abs contact">
    <div><svg width="9" height="6" viewBox="0 0 9 6"><rect width="9" height="6" fill="#0f3f78"/><path d="M0 0l4.5 3.5L9 0" stroke="#fff" stroke-width=".8" fill="none"/></svg>info@brevolank.com</div>
    <div class="phone"><svg width="9" height="8" viewBox="0 0 9 8"><rect x="0" y="2" width="9" height="6" rx="1" fill="#0f3f78"/><rect x="1" y="0" width="7" height="2.5" rx="1" fill="#0f3f78"/></svg>+1 555 014 2290</div>
  </div>
</header>

<nav class="abs main-nav">
  <a href="#">Home</a><a href="#">Product &amp; Services</a><a href="#">Corporate</a><a href="#">Careers</a><a href="#">Contact</a>
</nav>

<section>
  <div class="abs hero-frame"></div>
  <div class="abs hero" role="img" aria-label="Turbine machinery photo in dark grey tones"></div>
  <h1 class="abs hero-title">Conceptual Design and<br>Optimization of Turbomachinery</h1>
  <div class="abs hero-list">Turbomachinery design / Optimization Software<br>Classroom / Online training Courses<br>Consulting Services</div>
  <a class="abs btn btn-blue" href="#" style="left:108px;top:249px;width:63px;height:16px">Learn More »</a>
  <a class="abs btn btn-orange" href="#" style="left:180px;top:249px;width:81px;height:16px">Request a Quote</a>
  <div class="abs hero-shot" role="img" aria-label="Software screenshot showing a 3D impeller model and performance charts"></div>
  <div class="abs thumbs">
    <svg class="abs" style="left:2px;top:17px" width="8" height="12" viewBox="0 0 8 12"><path d="M7 1L2 6l5 5" stroke="#222" stroke-width="2.4" fill="none"/></svg>
    <div class="thumb active" style="left:21px" role="img" aria-label="Banner thumbnail: turbine software"></div>
    <div class="thumb" style="left:115px" role="img" aria-label="Banner thumbnail"></div>
    <div class="thumb" style="left:210px" role="img" aria-label="Banner thumbnail"></div>
    <div class="thumb" style="left:304px" role="img" aria-label="Banner thumbnail"></div>
    <div class="thumb" style="left:399px" role="img" aria-label="Banner thumbnail"></div>
    <svg class="abs" style="left:489px;top:17px" width="8" height="12" viewBox="0 0 8 12"><path d="M1 1l5 5-5 5" stroke="#222" stroke-width="2.4" fill="none"/></svg>
  </div>
</section>

<section class="abs welcome">
  <h2>Welcome to Brevolank</h2>
  <p>Lorem ipsum dolor sit amet, consectetuer adipiscing elit. Aenean commodo ligula eget dolor. Aenean massa. Cum sociis natoque penatibus et magnis dis parturient montes, nascetur ridiculus mus. Donec quam felis, ultricies nec, pellentesque eu, pretium quis, sem. Nulla consequat massa quis enim. Donec pede justo, fringilla vel, aliquet nec, vulputate eget, arcu. In enim justo, rhoncus ut, imperd<br>a, venenatis vitae, justo. Nullam dictum felis eu pede mollis pretium. Integer tincidunt. Cras dapibus. Etiam rhoncus. Maecenas tempus, tellus eget condimentum et magnis dis parturient montes, nascetur ridiculus mus. Donec quam felis, ultricies nec, pellentesque eu, pretium quis, sem. Nulla consequat massa quis enim. Donec pede justo, fringilla vel, aliquet nec, vulputate eget, arcu. In enim justo, rhoncus ut, imperdiet a, venenatis vitae, justo. Nullam dictum felis eu pede mollis pretium. Integer tincidunt. Cras dapibus. Vivamus elementum semper nisi. Aenean vulputate eleifend tellus. Aenean leo ligula, porttitor eu, consequat vitae, eleifend ac, enim. <a class="more" href="#">more »</a></p>
</section>

<aside class="abs demo">
  <div class="demo-head"><svg width="14" height="12" viewBox="0 0 14 12"><rect y="3" width="14" height="9" fill="#1d5a9c"/><path d="M0 3l2-3h12l-2 3z" fill="#333"/></svg>Schedule a Demo</div>
  <p>If you are interested in seeing one of our turbomachinery design products in action and want to schedule a demonstration, please fill out the form below and we will contact you to in order to coordinate a convenient date and time. All your information will remain confidential.</p>
  <a class="abs btn btn-blue" href="#" style="left:16px;top:112px;width:85px;height:18px">Request a Demo</a>
</aside>

<section class="abs column edu">
  <h2>Education Courses</h2>
  <ul>
    <li>Axial Turbine Fundamentals Course</li>
    <li>FlowPath Training Workshop for Professional Designers</li>
    <li>Axial Compressor Fundamentals Course</li>
    <li>Steam and Gas Turbine Design Training Course</li>
    <li>Online Training Courses</li>
    <li>Free 1-hour Webinar</li>
    <li>FlowPath Educational Version for Colleges and Universities</li>
    <li>FlowPath Lite</li>
  </ul>
  <a class="small-link" href="#" style="display:block;margin-top:14px">All Courses »</a>
</section>

<section>
  <h2 class="abs" style="left:257px;top:546px">Client Success Story</h2>
  <div class="abs dots"><i></i><i></i><i></i><i></i></div>
  <blockquote class="abs quote-box"><span class="quote-mark">“</span>Curabitur ligula sapien, tincidunt non, euismod vitae, posuere imperdiet, leo. Maecenas lesuada. Praesent congue erat at massa. Sed cursus turpis vitae tortor. Donec posuere vulputate arcu. Phasellus accumsan cursus velit. Vestibulum ante ipsum primis in faucibus.</blockquote>
  <svg class="abs" style="left:266px;top:665px" width="14" height="9" viewBox="0 0 14 9"><path d="M0 0h14L2 9z" fill="#fff" stroke="#ddd"/><path d="M0.5 0h13" stroke="#fff" stroke-width="2"/></svg>
  <div class="abs client-name">Halvorn</div>
  <div class="abs client-role"><b>Graham Lisle</b>, Director of Research Computing</div>
</section>

<section class="abs column feed">
  <h2>From Chirpline</h2>
  <div class="tweet"><svg width="8" height="7" viewBox="0 0 8 7"><path d="M0 4L6 0l2 3-5 4z" fill="#999"/></svg><p>Curabitur ligula sapien, tincidunt non, euis vitae, posuere imperdiet, leo. Maecenas lesuada. <a href="#">http://brv.to/R4xr</a></p></div>
  <div class="tweet"><svg width="8" height="7" viewBox="0 0 8 7"><path d="M0 4L6 0l2 3-5 4z" fill="#999"/></svg><p>Curabitur ligula sapien, tincidunt non, euis vitae, posuere imperdiet, leo. Maecenas lesuada. <a href="#">http://brv.to/R4xr</a></p></div>
  <div class="tweet"><svg width="8" height="7" viewBox="0 0 8 7"><path d="M0 4L6 0l2 3-5 4z" fill="#999"/></svg><p>Curabitur ligula sapien, tincidunt non, euis vitae, posuere imperdiet, leo. Maecenas lesuada. <a href="#">http://brv.to/R4xr</a></p></div>
  <a class="small-link" href="#" style="display:block;margin-top:12px;padding-left:15px">Join Conversation »</a>
</section>

<section class="abs card news">
  <h2>Company News</h2>
  <article class="news-item"><div class="date"><b>21</b><span>Apr</span></div><div><h3>Supercritical CO2 Cycle - Advanced Power Conversion Technology.</h3><p>On January 8th and 9th, 2013 Brevolank hosted a free one hour webinar called Supercritical CO2 Cycle - Advanced Power Conversion Technology ... <a class="more" href="#">more »</a></p></div></article>
  <article class="news-item"><div class="date"><b>21</b><span>Apr</span></div><div><h3>Supercritical CO2 Cycle - Advanced Power Conversion Technology.</h3><p>On January 8th and 9th, 2013 Brevolank hosted a free one hour webinar called Supercritical CO2 Cycle - Advanced Power Conversion Technology ... <a class="more" href="#">more »</a></p></div></article>
  <article class="news-item"><div class="date"><b>21</b><span>Apr</span></div><div><h3>Supercritical CO2 Cycle - Advanced Power Conversion Technology.</h3><p>On January 8th and 9th, 2013 Brevolank hosted a free one hour webinar called Supercritical CO2 Cycle - Advanced Power Conversion Technology ... <a class="more" href="#">more »</a></p></div></article>
  <a class="small-link" href="#" style="padding-left:2px">More News »</a>
</section>

<section class="abs card papers">
  <h2>White Papers</h2>
  <article class="paper"><span class="paper-icon"></span><div>A new method for centrifugal and mixed-type compressors flow paths design based on a unique integrated conceptual design environment is presented in this article. At the heart of this new method is the translation of proven, integrated design environments that have been successfully used for axial turbomachinery for many years. This integrated environment is a seamless and swift processing scheme that incorporates stages aerodynamic analysis and preliminary design/sizing based on the onedimensional method interactive spatial blade profiling, export of blade geometry to CAD and CFD tools, 3D stress and vibration analysis, and finally, flow<a class="download" href="#"><i></i>Download Whitepaper</a></div></article>
  <article class="paper"><span class="paper-icon"></span><div>A new method for centrifugal and mixed-type compressors flow paths design based on a unique integrated conceptual design environment is presented in this article. At the heart of this new method is the translation of proven, integrated design environments that have been successfully used for axial turbomachinery for many years.<a class="download" href="#"><i></i>Download Whitepaper</a></div></article>
  <a class="small-link" href="#" style="padding-left:2px">All Resources »</a>
</section>

<footer>
  <div class="abs footer"></div>
  <div class="abs footer-col" style="left:89px"><h4>COMPANY</h4><ul><li>Subscribe</li><li>Submit a Business Plan</li><li>Find a Distributor</li><li>Contact Tech Support</li><li>Submit a Resume</li><li>Schedule a Demo</li><li>Request a Quote</li></ul></div>
  <div class="abs footer-col" style="left:215px"><h4>CUSTOMERS</h4><ul><li>User Center</li><li>Animated Presentations</li><li>Career</li><li>Forum</li><li>News</li><li>Articles and Technical Papers</li><li>Sitemap</li></ul></div>
  <div class="abs footer-col" style="left:342px"><h4>PRODUCTS</h4><ul><li>Axial Turbines</li><li>Radial Turbines</li><li>Axial Compressors</li><li>Centrifugal Compressors</li><li>FlowSlice</li><li>FlowPath Axial Pump</li><li>Radial Pump</li></ul></div>
  <div class="abs footer-col" style="left:469px"><h4>COURCES</h4><ul><li>Training Courses Schedule</li><li>Online Courses</li><li>Webinar</li><li>FlowPath Trainning Workshop</li><li>Axial Turbine Fundamentals</li><li>Axial Compressor Fundamentals</li><li>Steam and Gas Turbine Design</li></ul></div>
  <div class="abs footer-bottom">
    <span class="copy">© 2013 Larkfield Email Marketing. All rights reserved</span>
    <span class="social">We are social: <i style="margin-left:6px"></i><i></i><i></i><i></i></span>
  </div>
</footer>

</body>
</html>
```